Skin care manufacturer looking for packaging design for new skin care brand.

We need a design and logo for a skin care brand to be sold at retail stores and online in the United States and Europe. The design will be for 1.7oz - 2oz serums that will not have a retail box. The name of the brand is Clear Meadow and should be a luxurious brand that is approachable. The brand will consist of 4 face serums - Vitamin C, Collagen, Retinol and Hyaluronic Acid. Images shown are for inspiration only. Color of bottles can be varied based on design and bottles can be screen printed or labeled.

Need extra days to review

Target Market(s)

Target market is 30+ female

Industry/Entity Type

Beauty

Requirements
Must have
• Ingredient call outs + benefit. Ex: Vitamin C Brightening Serum. Packaging should be translucent

```html
<!DOCTYPE html>
<html lang="en">
<head>
<meta charset="UTF-8">
<title>Clear Meadow – Vitamin C Brightening Serum</title>
<link href="https://fonts.googleapis.com/css2?family=Italiana&family=Montserrat:wght@300;400&display=swap" rel="stylesheet">
<style>
  :root {
    --backdrop: #d8cfc6;
    --glass: #eeeeee;
    --glass-edge: #dcdcdc;
    --collar: #c9c9cb;
    --collar-shine: #f4f4f6;
    --bulb: #f8f8f6;
    --ink: #1a1a1a;
    --accent-lime: #d6e04a;
    --accent-pink: #f2a9c9;
  }
  html, body {
    margin: 0;
    padding: 0;
    width: 1200px;
    height: 1200px;
    overflow: hidden;
    background: var(--backdrop);
  }
  .canvas {
    position: relative;
    width: 1200px;
    height: 1200px;
    background: var(--backdrop);
  }
  .bottle {
    position: absolute;
    left: 0;
    top: 0;
  }
  .label {
    position: absolute;
    left: 370px;
    width: 460px;
    text-align: center;
    color: var(--ink);
  }
  .brand-name {
    top: 520px;
    margin: 0;
    font-family: "Italiana", serif;
    font-weight: 400;
    font-size: 86px;
    line-height: 0.92;
    letter-spacing: -1px;
  }
  .botanical {
    position: absolute;
    left: 555px;
    top: 735px;
    width: 90px;
    height: 150px;
    border-radius: 45px 45px 20px 20px;
    background: linear-gradient(180deg, rgba(242,169,201,0.55), rgba(242,169,201,0.25));
  }
  .ingredient {
    top: 905px;
    font-family: "Montserrat", sans-serif;
    font-weight: 300;
    font-size: 22px;
    letter-spacing: 6px;
    color: var(--accent-lime);
  }
  .benefit {
    top: 940px;
    font-family: "Montserrat", sans-serif;
    font-weight: 400;
    font-size: 36px;
    line-height: 1.25;
    letter-spacing: 1.5px;
  }
  .volume {
    top: 1080px;
    font-family: "Montserrat", sans-serif;
    font-weight: 400;
    font-size: 22px;
  }
</style>
</head>
<body>
  <main class="canvas">
    <svg class="bottle" width="1200" height="1200" viewBox="0 0 1200 1200" aria-hidden="true">
      <defs>
        <linearGradient id="glassTone" x1="0" x2="1" y1="0" y2="0">
          <stop offset="0" stop-color="#e2e2e2"/>
          <stop offset="0.35" stop-color="#f4f4f4"/>
          <stop offset="0.8" stop-color="#ededed"/>
          <stop offset="1" stop-color="#d9d9d9"/>
        </linearGradient>
        <linearGradient id="collarTone" x1="0" x2="1" y1="0" y2="0">
          <stop offset="0" stop-color="#a9a9ac"/>
          <stop offset="0.3" stop-color="#f4f4f6"/>
          <stop offset="0.55" stop-color="#c4c4c7"/>
          <stop offset="0.8" stop-color="#eeeeef"/>
          <stop offset="1" stop-color="#9d9da0"/>
        </linearGradient>
      </defs>
      <rect class="dropper-bulb" x="545" y="90" width="110" height="200" rx="55" fill="#f8f8f6"/>
      <rect class="dropper-base" x="530" y="250" width="140" height="50" rx="10" fill="#f2f2f0"/>
      <rect class="collar" x="510" y="295" width="180" height="95" rx="6" fill="url(#collarTone)"/>
      <path class="glass-body" d="M530 390 L670 390 L670 420 C 800 440 830 500 830 560 L830 1120 C 830 1145 810 1160 785 1160 L415 1160 C 390 1160 370 1145 370 1120 L370 560 C 370 500 400 440 530 420 Z" fill="url(#glassTone)"/>
    </svg>

    <h1 class="label brand-name">Clear<br>Meadow</h1>
    <div class="botanical" role="img" aria-label="Delicate pink line-drawn flower sprig illustration"></div>
    <div class="label ingredient">VITAMIN C</div>
    <div class="label benefit">BRIGHTENING<br>SERUM</div>
    <div class="label volume">1.7oz</div>
  </main>
</body>
</html>
```